Design of Labels for Harbour Mast Spirit bottle

Design bottle labels for Harbour Mast Spirit. There are three labels to design; a front, a back and a tamper band to be placed over the cork. The labels should be deigned to fit the bottle specified in the link below.
The Gin is an excellent high end premium brand Navy strength Gin 57% Vol. The bottle should evoke excellence and a romance of period of pride in the British Navy. Gin was drunk by officers in the Navy so a representation of the Officer Class should be made possibly through gold braid of a senior officer's sleeve, cap or lapel. The white ensign should also be prominent. Suggested colour themes are navy blues, grey, and white....although others schemes may be suitable. Crowfield Deck Cordial is a good example of the sort of thing we are looking for, although the design must not be so similar that it encroaches on Crowfield's trade mark or copyrights. The period theme is 1900 to 1940
Bottle link: https://www.vessel-ware-depot.co.uk/Glass-bottles/350ml-flint-glass-bottle-Mirren.html
Target Market(s)
Gin Drinkers
Look and feel
Each slider illustrates characteristics of the customer's brand and the style your logo design should communicate.

```html
<!DOCTYPE html>
<html lang="en">
<head>
<meta charset="utf-8">
<title>Harbour Mast Spirit – Front Label</title>
<link rel="stylesheet" href="https://fonts.googleapis.com/css2?family=Cinzel:wght@600;700&family=Pinyon+Script&family=Oswald:wght@400&display=swap">
<style>
  :root {
    --backdrop: #b4b4b4;
    --paper-top: #f4f5fb;
    --paper-bottom: #e4e6f2;
    --navy: #1b2650;
    --navy-deep: #141d40;
    --ink: #232c4d;
    --gold: #c9ac5c;
    --gold-pale: #e2cf8e;
    --frame-light: #9aa0b4;
    --white: #ffffff;
    --flag-white: #eceef3;
  }
  html, body {
    margin: 0;
    padding: 0;
    width: 1200px;
    height: 1200px;
    overflow: hidden;
    background: var(--backdrop);
  }
  .stage {
    width: 1200px;
    height: 1200px;
    display: flex;
    align-items: center;
    justify-content: center;
  }
  .front-label { display: block; }
  .brand-arch {
    font-family: "Cinzel", serif;
    font-weight: 700;
    font-size: 84px;
    letter-spacing: 6px;
    fill: var(--ink);
  }
  .est-tag {
    font-family: "Cinzel", serif;
    font-weight: 600;
    font-size: 15px;
    fill: var(--white);
    letter-spacing: 1px;
  }
  .brand-name {
    font-family: "Cinzel", serif;
    font-weight: 700;
    font-size: 74px;
    fill: var(--white);
    letter-spacing: 1px;
  }
  .tagline {
    font-family: "Pinyon Script", cursive;
    font-size: 50px;
    fill: var(--gold);
  }
  .spec-line {
    font-family: "Oswald", sans-serif;
    font-size: 20px;
    fill: var(--gold-pale);
    letter-spacing: 0.5px;
  }
</style>
</head>
<body>
<main class="stage">
  <svg class="front-label" width="690" height="1040" viewBox="0 0 690 1040" aria-label="Harbour Mast Spirit front label">
    <defs>
      <linearGradient id="paper" x1="0" y1="0" x2="0" y2="1">
        <stop offset="0" stop-color="var(--paper-top)"/>
        <stop offset="1" stop-color="var(--paper-bottom)"/>
      </linearGradient>
      <linearGradient id="navyPanel" x1="0" y1="0" x2="0" y2="1">
        <stop offset="0" stop-color="var(--navy)"/>
        <stop offset="1" stop-color="var(--navy-deep)"/>
      </linearGradient>
      <radialGradient id="crestTone" cx="0.5" cy="0.5" r="0.6">
        <stop offset="0" stop-color="#d8c27a"/>
        <stop offset="0.55" stop-color="#8a8f9f"/>
        <stop offset="1" stop-color="#2c3558"/>
      </radialGradient>
      <linearGradient id="ensignTone" x1="0" y1="0" x2="1" y2="0">
        <stop offset="0" stop-color="#3a4f8f"/>
        <stop offset="0.35" stop-color="#c9c9d2"/>
        <stop offset="1" stop-color="#e6e6ea"/>
      </linearGradient>
      <path id="archPath" d="M 120 300 A 240 240 0 0 1 570 300"/>
      <clipPath id="labelShape">
        <rect x="0" y="0" width="690" height="1040" rx="26"/>
      </clipPath>
    </defs>

    <g clip-path="url(#labelShape)">
      <!-- paper panel -->
      <rect class="paper-panel" x="0" y="0" width="690" height="520" fill="url(#paper)"/>
      <!-- navy panel -->
      <rect class="navy-panel" x="0" y="520" width="690" height="520" fill="url(#navyPanel)"/>
    </g>

    <!-- frame -->
    <rect class="label-frame" x="26" y="26" width="638" height="988" rx="10" fill="none" stroke="var(--frame-light)" stroke-width="8"/>
    <rect class="label-frame-inner" x="38" y="38" width="614" height="964" rx="6" fill="none" stroke="var(--ink)" stroke-width="1.5" opacity="0.6"/>

    <!-- arched name -->
    <text class="brand-arch"><textPath href="#archPath" startOffset="50%" text-anchor="middle">HARBOUR</textPath></text>

    <!-- crest emblem area -->
    <rect class="crest-area" x="175" y="225" width="340" height="270" rx="40" fill="url(#crestTone)" role="img" aria-label="Naval crest with crown, crossed anchors, rope ring and two rampant lions in gold and navy"/>

    <!-- est tags -->
    <rect class="est-box" x="66" y="316" width="64" height="26" fill="var(--frame-light)"/>
    <text class="est-tag" x="98" y="335" text-anchor="middle">EST.</text>
    <rect class="est-box" x="560" y="316" width="64" height="26" fill="var(--frame-light)"/>
    <text class="est-tag" x="592" y="335" text-anchor="middle">2018</text>

    <!-- ensign area -->
    <rect class="ensign-area" x="215" y="560" width="260" height="160" rx="12" fill="url(#ensignTone)" role="img" aria-label="Waving white ensign flag with red cross and union canton"/>

    <!-- name -->
    <text class="brand-name" x="345" y="815" text-anchor="middle">MAST SPIRIT</text>
    <text class="tagline" x="345" y="885" text-anchor="middle">Premium Blend</text>

    <line class="spec-rule" x1="100" y1="922" x2="590" y2="922" stroke="var(--frame-light)" stroke-width="1.5"/>
    <text class="spec-line" x="110" y="962">57 % vol</text>
    <text class="spec-line" x="345" y="962" text-anchor="middle">PRODUCT OF ENGLAND</text>
    <text class="spec-line" x="580" y="962" text-anchor="end">350 ml</text>
  </svg>
</main>
</body>
</html>
```